Corporate Vision/Mission Designs for the Office Walls

What we are looking for:

We are looking for design proposals to frame our mission, vision and values on our office walls

The designs need to be elegant, clean lines, simple, easy to follow and of course, should follow our brand guidelines.

Here's the copy:

For Boardoom:
Vision: Marlow Brightside ignites people with passion enabling joy and lifetime memories

Mission: We are transforming the way property is bought.

For Garage
Purpose: We connect people with their dreams, turn dreams into reality.

For Entrance
Core Values
Honour
Passion
Sharing
Surprise
Fun

Vision & Mission will go in the boardroom
Core Values : at the Entrance
Purpose: in the Garage meeting room

Attachments to this project include:

a) Photos of the walls where they will go, and the current designs on the walls

b) brand guidelines

Industry/Entity Type

Office

Font styles to use
Decorative

Requirements
Must have
• Follow the brandguidelines, and colors.
• Green / use minimally

```html
<!DOCTYPE html>
<html lang="en">
<head>
<meta charset="UTF-8">
<title>Purpose – Garage Meeting Room Wall</title>
<link href="https://fonts.googleapis.com/css2?family=Alegreya+Sans:ital,wght@1,500&family=Tenor+Sans&display=swap" rel="stylesheet">
<style>
  :root {
    --wall: #f6f5f3;
    --teal: #16b2ae;
    --ink: #55545b;
  }
  * { margin: 0; padding: 0; box-sizing: border-box; }
  html, body {
    width: 1200px;
    height: 900px;
    overflow: hidden;
    background: var(--wall);
  }
  .wall-panel {
    position: relative;
    width: 1200px;
    height: 900px;
    background: var(--wall);
  }
  .heading-bar {
    position: absolute;
    left: 274px;
    top: 288px;
    width: 12px;
    height: 46px;
    background: var(--teal);
  }
  .heading {
    position: absolute;
    left: 322px;
    top: 276px;
    font-family: "Alegreya Sans", sans-serif;
    font-style: italic;
    font-weight: 500;
    font-size: 54px;
    line-height: 1;
    color: var(--teal);
  }
  .statement {
    position: absolute;
    left: 284px;
    top: 368px;
    font-family: "Tenor Sans", sans-serif;
    font-size: 36px;
    line-height: 48px;
    letter-spacing: -1.4px;
    color: var(--ink);
    text-transform: uppercase;
    white-space: nowrap;
  }
  .accent-rule {
    position: absolute;
    left: 871px;
    top: 408px;
    width: 2px;
    height: 84px;
    background: var(--teal);
  }
</style>
</head>
<body>
  <main class="wall-panel">
    <span class="heading-bar"></span>
    <h1 class="heading">Purpose</h1>
    <p class="statement">We connect people with<br>their dreams, turn dreams<br>into reality.</p>
    <span class="accent-rule"></span>
  </main>
</body>
</html>
```